Business Card Design Project

Bold, modern, clean business card design needed. Prefer double sided with art logo on the back. Front of card with company name logo, no art.

Target Market(s)

Our consulting company supports local, state and federal law enforcement officers. Therefore the design should be clean and direct with no flash or arrogance to it.

Industry/Entity Type

Business

```html
<!DOCTYPE html>
<html lang="en">
<head>
<meta charset="utf-8">
<title>Castell Systems – Business Card</title>
<link rel="stylesheet" href="https://fonts.googleapis.com/css2?family=Source+Sans+3:wght@400;600&family=Questrial&display=swap">
<style>
  :root {
    --backdrop: #3b2c20;
    --card: #ffffff;
    --ink: #111111;
    --lime: #9bc83f;
    --shadow: rgba(0, 0, 0, 0.45);
  }
  html, body {
    margin: 0;
    padding: 0;
    width: 1200px;
    height: 1000px;
    overflow: hidden;
    background: var(--backdrop);
  }
  .canvas {
    position: relative;
    width: 1200px;
    height: 1000px;
  }
  .card {
    position: absolute;
    left: 265px;
    width: 666px;
    height: 397px;
    background: var(--card);
    box-shadow: 0 4px 14px var(--shadow);
    overflow: hidden;
  }
  .card-front { top: 73px; }
  .card-back { top: 532px; }

  /* Front: brand name in place of the mark */
  .front-brand {
    position: absolute;
    inset: 0;
    display: flex;
    align-items: center;
    justify-content: center;
    gap: 16px;
  }
  .front-brand .brand-square {
    width: 28px;
    height: 28px;
    background: var(--lime);
  }
  .front-brand .brand-name {
    font-family: "Source Sans 3", sans-serif;
    font-weight: 600;
    font-size: 40px;
    letter-spacing: 4px;
    color: var(--ink);
    text-transform: uppercase;
  }

  /* Back */
  .wordmark {
    position: absolute;
    left: 23px;
    top: 58px;
    font-family: "Source Sans 3", sans-serif;
    font-weight: 600;
    font-size: 40px;
    line-height: 1.05;
    letter-spacing: 5px;
    color: var(--ink);
    text-transform: uppercase;
    margin: 0;
  }
  .person {
    position: absolute;
    left: 24px;
    top: 176px;
    font-family: "Source Sans 3", sans-serif;
  }
  .person .person-name {
    font-size: 24px;
    color: var(--ink);
    line-height: 1.1;
  }
  .person .person-role {
    font-size: 19px;
    color: var(--lime);
    line-height: 1.2;
  }
  .contacts {
    position: absolute;
    left: 24px;
    top: 267px;
    margin: 0;
    padding: 0;
    list-style: none;
    font-family: "Questrial", sans-serif;
    font-size: 18px;
    color: var(--ink);
  }
  .contacts li {
    display: flex;
    align-items: center;
    gap: 9px;
    height: 25px;
  }
  .contacts svg { width: 14px; height: 14px; fill: var(--lime); }
  .address {
    position: absolute;
    right: 24px;
    top: 292px;
    text-align: right;
    font-family: "Questrial", sans-serif;
    font-size: 18px;
    line-height: 25px;
    color: var(--ink);
  }
  .footer-bands {
    position: absolute;
    left: 0;
    bottom: 0;
    width: 666px;
    height: 30px;
  }
  .website {
    position: absolute;
    right: 58px;
    bottom: 6px;
    font-family: "Questrial", sans-serif;
    font-size: 18px;
    color: #ffffff;
  }
</style>
</head>
<body>
<div class="canvas">

  <section class="card card-front" aria-label="Card front">
    <div class="front-brand">
      <span class="brand-square"></span>
      <span class="brand-name">Castell Systems</span>
    </div>
  </section>

  <section class="card card-back" aria-label="Card back">
    <h1 class="wordmark">Castell<br>Systems</h1>

    <div class="person">
      <div class="person-name">Daniel Ortway</div>
      <div class="person-role">Managing Director</div>
    </div>

    <ul class="contacts">
      <li>
        <svg viewBox="0 0 14 14" aria-hidden="true"><path d="M4 0h6a1 1 0 0 1 1 1v12a1 1 0 0 1-1 1H4a1 1 0 0 1-1-1V1a1 1 0 0 1 1-1zm0.5 1.5v10h5v-10z"/></svg>
        <span>+61 400 555 018</span>
      </li>
      <li>
        <svg viewBox="0 0 14 14" aria-hidden="true"><path d="M1 4c0-1.5 2.5-2.5 6-2.5s6 1 6 2.5v1.2h-3V4H4v1.2H1z"/><path d="M3 6.5h8l1.5 6h-11z"/></svg>
        <span>+61 3 9555 0142</span>
      </li>
      <li>
        <svg viewBox="0 0 14 14" aria-hidden="true"><path d="M0 3h14v1L7 8.5 0 4z"/><path d="M0 5.5l7 4.5 7-4.5V11H0z"/></svg>
        <span>daniel@castellsystems.com</span>
      </li>
    </ul>

    <div class="address">14 Harlow Street Kingsford<br>VIC 3820</div>

    <svg class="footer-bands" viewBox="0 0 666 30" aria-hidden="true">
      <polygon points="0,7 399,7 396,12 0,12" fill="var(--ink)"/>
      <polygon points="0,21 666,21 666,30 0,30" fill="var(--lime)"/>
      <polygon points="386,0 666,0 666,30 371,30" fill="var(--lime)"/>
    </svg>
    <div class="website">www.castellsys.com</div>
  </section>

</div>
</body>
</html>
```